Quill Ridge Business cards

We need business cards for our aviation company called Quill Ridge Aviation. The colour scheme is the same as the one in the logo you design (metallic green/ similar to the colours on the aircraft). The design needs to be unique and stand out.

Industry/Entity Type

Business

```html
<!DOCTYPE html>
<html lang="en">
<head>
<meta charset="utf-8">
<title>Quill Ridge Aviation – Business Cards</title>
<link href="https://fonts.googleapis.com/css2?family=Exo+2:wght@700&family=Roboto+Condensed:wght@400;500&display=swap" rel="stylesheet">
<style>
  :root {
    --backdrop: #8e8e8e;
    --card: #ffffff;
    --green-dark: #0b6b3a;
    --green: #1a8a4e;
    --green-light: #5cc58c;
    --ink: #444444;
    --shadow: rgba(0, 0, 0, 0.35);
  }
  * { margin: 0; padding: 0; box-sizing: border-box; }
  html, body {
    width: 1200px;
    height: 1000px;
    overflow: hidden;
    background: var(--backdrop);
  }
  .canvas {
    position: relative;
    width: 1200px;
    height: 1000px;
  }
  .card {
    position: absolute;
    top: 341px;
    width: 542px;
    height: 318px;
    background: var(--card);
    box-shadow: 2px 3px 6px var(--shadow);
  }
  .card--front { left: 42px; }
  .card--back { left: 628px; }

  /* Front */
  .wing-art {
    position: absolute;
    left: 0;
    top: 34px;
    width: 232px;
    height: 284px;
    background: linear-gradient(160deg, var(--green-light) 0%, var(--green) 45%, var(--green-dark) 100%);
    border-radius: 0 90% 0 0 / 0 100% 0 0;
    opacity: 0.9;
  }
  .holder-name {
    position: absolute;
    left: 270px;
    top: 30px;
    font-family: "Exo 2", sans-serif;
    font-weight: 700;
    font-size: 24px;
    letter-spacing: 0.5px;
    color: var(--green);
  }
  .holder-role {
    position: absolute;
    left: 271px;
    top: 59px;
    font-family: "Roboto Condensed", sans-serif;
    font-size: 13px;
    color: var(--ink);
  }
  .contact-list {
    position: absolute;
    left: 269px;
    top: 151px;
    list-style: none;
    font-family: "Roboto Condensed", sans-serif;
    font-size: 14px;
    color: var(--ink);
  }
  .contact-list li {
    display: flex;
    align-items: center;
    height: 23px;
  }
  .contact-icon {
    width: 16px;
    height: 16px;
    margin-right: 6px;
    flex: none;
  }

  /* Back */
  .brand {
    position: absolute;
    left: 0;
    right: 0;
    top: 140px;
    display: flex;
    justify-content: center;
    align-items: center;
    gap: 12px;
  }
  .brand-dot {
    width: 26px;
    height: 26px;
    border-radius: 50%;
    background: var(--green);
  }
  .brand-name {
    font-family: "Roboto Condensed", sans-serif;
    font-weight: 500;
    font-size: 30px;
    text-transform: uppercase;
    color: var(--green);
  }
</style>
</head>
<body>
<svg width="0" height="0" style="position:absolute">
  <defs>
    <linearGradient id="icon-fill" x1="0" y1="0" x2="1" y2="1">
      <stop offset="0" stop-color="#5cc58c"/>
      <stop offset="1" stop-color="#0b6b3a"/>
    </linearGradient>
  </defs>
</svg>
<main class="canvas">
  <section class="card card--front">
    <div class="wing-art" role="img" aria-label="Large green metallic wing emblem decoration"></div>
    <h1 class="holder-name">Martin Hollis</h1>
    <p class="holder-role">Managing Director</p>
    <ul class="contact-list">
      <li>
        <svg class="contact-icon" viewBox="0 0 16 16" aria-hidden="true"><rect width="16" height="16" rx="3" fill="url(#icon-fill)"/><rect x="5" y="3" width="6" height="10" rx="1" fill="none" stroke="#fff" stroke-width="1.2"/><circle cx="8" cy="11" r="0.8" fill="#fff"/></svg>
        +0 412.555.0193
      </li>
      <li>
        <svg class="contact-icon" viewBox="0 0 16 16" aria-hidden="true"><rect width="16" height="16" rx="3" fill="url(#icon-fill)"/><path d="M5 3.5 L7 5.5 L6 7 Q7.5 9.5 9 10 L10.5 9 L12.5 11 L11 12.5 Q6 12 3.5 5 Z" fill="#fff"/></svg>
        +0 412.555.0194
      </li>
      <li>
        <svg class="contact-icon" viewBox="0 0 16 16" aria-hidden="true"><rect width="16" height="16" rx="3" fill="url(#icon-fill)"/><rect x="4" y="6" width="8" height="6" fill="none" stroke="#fff" stroke-width="1.2"/><rect x="5.5" y="3.5" width="5" height="2.5" fill="#fff"/></svg>
        +0 412.555.0195
      </li>
      <li>
        <svg class="contact-icon" viewBox="0 0 16 16" aria-hidden="true"><rect width="16" height="16" rx="3" fill="url(#icon-fill)"/><rect x="3.5" y="5" width="9" height="6.5" fill="none" stroke="#fff" stroke-width="1.2"/><path d="M3.5 5 L8 9 L12.5 5" fill="none" stroke="#fff" stroke-width="1.2"/></svg>
        mail@quillridgeair.com
      </li>
      <li>
        <svg class="contact-icon" viewBox="0 0 16 16" aria-hidden="true"><rect width="16" height="16" rx="3" fill="url(#icon-fill)"/><circle cx="8" cy="8" r="4.5" fill="none" stroke="#fff" stroke-width="1.1"/><ellipse cx="8" cy="8" rx="2" ry="4.5" fill="none" stroke="#fff" stroke-width="1"/><path d="M3.5 8 H12.5" stroke="#fff" stroke-width="1"/></svg>
        www.quillridgeair.com
      </li>
      <li>
        <svg class="contact-icon" viewBox="0 0 16 16" aria-hidden="true"><rect width="16" height="16" rx="3" fill="url(#icon-fill)"/><path d="M8 13 Q4 8.5 4 6.5 A4 4 0 0 1 12 6.5 Q12 8.5 8 13 Z" fill="#fff"/><circle cx="8" cy="6.5" r="1.5" fill="#1a8a4e"/></svg>
        12 Harbour Lane, Kestrel Bay, WA, 6000
      </li>
    </ul>
  </section>

  <section class="card card--back">
    <div class="brand">
      <span class="brand-dot" aria-hidden="true"></span>
      <span class="brand-name">Quill Ridge Aviation</span>
    </div>
  </section>
</main>
</body>
</html>
```